Contemporary Elegant Business Card Design for an International Trade Company in the Wine Industry

We need a new business card design for an international trade company in the wine and winemaking industry. The overall feel of the card should be contemporary, upscale, luxurious and elegant. It should communicate confidence and professionalism. The colors should complementary to our logo design (burgundy, gold, and black).
Inspiration: rich velvet tapestry
The card should include the following information:
Business: Brovenna Trading/Shipping, LLC.
Name: Marcus T. Hollenbrand
Title: CEO
Email: mark@brovennatrading.example
Phone: 555-294-6172
www.brovennatrading.example
Updates
Project Deadline Extended
Reason: We'd like the designers that we requested some additional designs from to still submit designs. Thank you!
Industry/Entity Type
Business
Contact Information for Business Card
Title: CEO
Phone: 555-294-6172
www.brovennatrading.example
Look and feel

```html
<!DOCTYPE html>
<html lang="en">
<head>
<meta charset="utf-8">
<title>Brovenna Trading/Shipping – Business Card</title>
<link rel="stylesheet" href="https://fonts.googleapis.com/css2?family=Open+Sans:wght@400;600;700&display=swap">
<style>
  :root {
    --backdrop: #3a302b;
    --card-front: #2e2820;
    --card-front-light: #3c3428;
    --card-back: #151515;
    --gold: #d99a2b;
    --burgundy: #7a1620;
    --text-light: #f4efe6;
    --text-muted: #e6ded0;
  }
  * { box-sizing: border-box; margin: 0; padding: 0; }
  html, body { width: 1200px; height: 844px; overflow: hidden; }
  body {
    background: var(--backdrop);
    font-family: "Open Sans", sans-serif;
    position: relative;
  }
  .card {
    position: absolute;
    top: 272px;
    width: 525px;
    height: 300px;
    overflow: hidden;
  }
  .card--front { left: 50px; background: var(--card-front); }
  .card--back  { left: 625px; background: var(--card-back); }

  .front-texture {
    position: absolute;
    inset: 0;
    background: radial-gradient(ellipse at 70% 30%, var(--card-front-light) 0%, var(--card-front) 70%);
  }
  .gold-band {
    position: absolute;
    left: 0; right: 0;
    height: 12px;
    background: var(--gold);
  }
  .gold-band--top { top: 10px; }
  .gold-band--bottom { bottom: 10px; }

  .contact-block {
    position: absolute;
    left: 0; right: 0;
    top: 78px;
    text-align: center;
    color: var(--text-light);
  }
  .person-name {
    font-size: 19px;
    font-weight: 700;
    letter-spacing: 0.2px;
  }
  .name-rule {
    width: 170px;
    height: 1px;
    margin: 5px auto 6px;
    background: var(--gold);
  }
  .person-title {
    font-size: 13px;
    font-weight: 400;
    color: var(--text-muted);
  }
  .contact-list {
    list-style: none;
    margin-top: 40px;
    font-size: 14px;
    line-height: 21px;
    color: var(--text-muted);
  }

  .brand-lockup {
    position: absolute;
    left: 50%; top: 50%;
    transform: translate(-50%, -50%);
    display: flex;
    align-items: center;
    gap: 14px;
  }
  .brand-square {
    width: 44px; height: 44px;
    background: var(--burgundy);
  }
  .brand-name {
    font-size: 30px;
    font-weight: 700;
    letter-spacing: 1px;
    color: var(--text-light);
  }
  .edge-tab {
    position: absolute;
    width: 40px;
    height: 34px;
    background: var(--burgundy);
  }
  .edge-tab::after {
    content: "";
    position: absolute;
    top: 0; bottom: 0;
    width: 4px;
    background: var(--gold);
  }
  .edge-tab--top-right { right: 0; top: 26px; }
  .edge-tab--top-right::after { left: 8px; }
  .edge-tab--mid-left { left: 0; top: 160px; }
  .edge-tab--mid-left::after { right: 8px; }
</style>
</head>
<body>
  <section class="card card--front" aria-label="Business card front">
    <div class="front-texture" role="img" aria-label="Faint world map texture in dark brown tones"></div>
    <div class="gold-band gold-band--top"></div>
    <div class="gold-band gold-band--bottom"></div>
    <div class="contact-block">
      <h1 class="person-name">Marcus T. Hollenbrand</h1>
      <div class="name-rule"></div>
      <p class="person-title">CEO</p>
      <ul class="contact-list">
        <li>555-294-6172</li>
        <li>mark@brovennatrading.example</li>
        <li>www.brovennatrading.example</li>
      </ul>
    </div>
  </section>

  <section class="card card--back" aria-label="Business card back">
    <div class="edge-tab edge-tab--top-right"></div>
    <div class="edge-tab edge-tab--mid-left"></div>
    <div class="brand-lockup">
      <div class="brand-square"></div>
      <span class="brand-name">BROVENNA</span>
    </div>
  </section>
</body>
</html>
```